Redesign existing website

We would like a redesign of the website http://www.velbrisanalytics.com that creates a more modern, up to date look.

Velbris Analytics creates software for social science research and is focused on making the software user friendly and easy to use. We would like to convey seriousness, but also
a very up to date, just released look.

Feel free to modify the logo if you wish.

Target Market(s)

Academics, researchers

Industry/Entity Type

Software

Requirements
Must have
• The design should incorporate the same information as the current website.

```html
<!DOCTYPE html>
<html lang="en">
<head>
<meta charset="utf-8">
<title>Velbris Analytics – Website Redesign</title>
<link href="https://fonts.googleapis.com/css2?family=Oswald:wght@300;400&family=PT+Serif:ital@1&family=Arimo:wght@400;700&display=swap" rel="stylesheet">
<style>
  :root {
    --sheet-bg: #ffffff;
    --accent-blue: #3aa3c8;
    --accent-orange: #ff6b00;
    --slate-backdrop: #2b2c2d;
    --stone-backdrop: #dddbd6;
    --light-panel: #dadada;
    --light-news: #efefef;
    --dark-panel: #232323;
    --dark-news: #111111;
  }
  * { margin: 0; padding: 0; box-sizing: border-box; }
  html, body { width: 773px; height: 1200px; overflow: hidden; background: var(--sheet-bg); }
  .sheet { position: relative; width: 773px; height: 1200px; }

  .theme-light {
    --accent: var(--accent-blue);
    --backdrop: var(--slate-backdrop);
    --panel: var(--light-panel);
    --news-bg: var(--light-news);
    --ink: #111;
    --body-ink: #333;
    --muted-ink: #555;
    --cta-bg: #ffffff;
    --cta-border: #666;
    --rule: #bdbdbd;
    --mark: #3f3f3f;
    --arrow: #9a9a9a;
  }
  .theme-dark {
    --accent: var(--accent-orange);
    --backdrop: var(--stone-backdrop);
    --panel: var(--dark-panel);
    --news-bg: var(--dark-news);
    --ink: #f2f2f2;
    --body-ink: #d0d0d0;
    --muted-ink: #bdbdbd;
    --cta-bg: #000000;
    --cta-border: #bbbbbb;
    --rule: #3a3a3a;
    --mark: #bdbdbd;
    --arrow: #555;
  }

  .site-view { position: absolute; left: 0; width: 773px; height: 411px; overflow: hidden; }
  .site-view.top { top: 0; }
  .site-view.bottom { top: 789px; }

  .band { position: absolute; left: 0; top: 0; width: 773px; height: 47px; background: var(--accent); border-bottom: 1px solid rgba(0,0,0,.35); }
  .backdrop { position: absolute; left: 0; top: 47px; width: 773px; height: 364px; background: var(--backdrop); }
  .panel { position: absolute; left: 138px; top: 47px; width: 496px; height: 364px; background: var(--panel); }
  .panel-rules { position: absolute; left: 138px; top: 56px; width: 496px; height: 6px; border-top: 1px solid var(--rule); border-bottom: 1px solid var(--rule); }
  .panel-foot { position: absolute; left: 152px; top: 362px; width: 468px; border-top: 1px solid var(--rule); }

  .main-nav { position: absolute; top: 71px; right: 190px; display: flex; gap: 6px; font: 400 9px/1 "Oswald", sans-serif; color: var(--ink); white-space: nowrap; }
  .main-nav .current { color: var(--accent); }

  .brand-mark { position: absolute; left: 194px; top: 84px; width: 34px; height: 34px; border-radius: 50%; background: var(--mark); }
  .brand-name { position: absolute; left: 169px; top: 121px; font: 400 10px/1 "Oswald", sans-serif; color: var(--accent); letter-spacing: .2px; white-space: nowrap; }

  .headline { position: absolute; left: 279px; top: 115px; width: 322px; font: 400 17.5px/1 "Oswald", sans-serif; color: var(--ink); letter-spacing: 0; white-space: nowrap; }

  .tagline { position: absolute; left: 167px; top: 165px; font: italic 11.5px/17.5px "PT Serif", serif; color: var(--muted-ink); }

  .mission { position: absolute; left: 167px; top: 218px; width: 310px; font: 400 6.4px/7.2px "Arimo", sans-serif; color: var(--body-ink); }
  .mission p + p { margin-top: 6px; }

  .news { position: absolute; left: 489px; top: 152px; width: 111px; height: 211px; background: var(--news-bg); padding: 8px 9px; }
  .news h2 { font: 400 14px/1 "Oswald", sans-serif; color: var(--accent); margin-bottom: 9px; letter-spacing: .3px; }
  .news-item { font: 400 6.3px/7.1px "Arimo", sans-serif; color: var(--body-ink); margin-bottom: 6px; }
  .news-item strong { font-weight: 700; display: block; }

  .cta { position: absolute; left: 167px; top: 282px; width: 234px; height: 66px; background: var(--cta-bg); border: 1px solid var(--cta-border); text-align: center; padding-top: 9px; font: 400 11px/17.5px "Oswald", sans-serif; color: var(--ink); letter-spacing: .2px; }
  .cta .product { color: var(--accent); font-weight: 300; }

  .cta-arrow { position: absolute; left: 414px; top: 315px; }

  .team-photo { position: absolute; left: 451px; top: 283px; width: 97px; height: 64px; border: 1px solid #555; background: linear-gradient(120deg, #3a3a3a 0%, #8d8d8d 35%, #d9d9d9 70%, #f3f3f3 100%); }
</style>
</head>
<body>
<div class="sheet">

  <section class="site-view top theme-light" aria-label="Home page, light colour scheme">
    <div class="band"></div>
    <div class="backdrop"></div>
    <div class="panel"></div>
    <div class="panel-rules"></div>
    <nav class="main-nav"><span class="current">HOME</span><span>PRODUCTS</span><span>NEWS</span><span>ABOUT US</span><span>CONTACT</span></nav>
    <div class="brand-mark"></div>
    <div class="brand-name">VELBRIS ANALYTICS</div>
    <h1 class="headline">EMPOWERING THE SOCIAL SCIENCE RESEARCHER</h1>
    <p class="tagline">Increasing the power and efficiency of<br>Empirical Social Science Research</p>
    <div class="mission">
      <p>The mission of Velbris Analytics, Inc. is to produce software products that multiply the power and efficiency of empirical scientific research in the social sciences.</p>
      <p>A central goal is to expand access to complex data sources and to the advanced methods of scientific investigation needed to analyze them.</p>
    </div>
    <aside class="news">
      <h2>NEWS</h2>
      <p class="news-item"><strong>April, 2009</strong>An early access preview of the Velbris Data Manager is available.</p>
      <p class="news-item"><strong>May, 2008</strong>Plenary Session by Miriam Halvorsen - New approaches to complex data management</p>
      <p class="news-item">34TH ANNUAL CONFERENCE<br>IADSR 2008<br>May 27-30, 2008</p>
    </aside>
    <div class="cta">Preview Release Available!<br><span class="product">Velbris Data Manager</span><br>Download Preview Release</div>
    <svg class="cta-arrow" width="26" height="18" viewBox="0 0 26 18" aria-hidden="true"><path d="M1 1h6l8 8-8 8H1l8-8z M11 1h6l8 8-8 8h-6l8-8z" fill="var(--arrow)"/></svg>
    <div class="team-photo" role="img" aria-label="Black and white photo of a smiling businesswoman with colleagues behind her"></div>
    <div class="panel-foot"></div>
  </section>

  <section class="site-view bottom theme-dark" aria-label="Home page, dark colour scheme">
    <div class="band"></div>
    <div class="backdrop"></div>
    <div class="panel"></div>
    <div class="panel-rules"></div>
    <nav class="main-nav"><span class="current">HOME</span><span>PRODUCTS</span><span>NEWS</span><span>ABOUT US</span><span>CONTACT</span></nav>
    <div class="brand-mark"></div>
    <div class="brand-name">VELBRIS ANALYTICS</div>
    <h1 class="headline">EMPOWERING THE SOCIAL SCIENCE RESEARCHER</h1>
    <p class="tagline">Increasing the power and efficiency of<br>Empirical Social Science Research</p>
    <div class="mission">
      <p>The mission of Velbris Analytics, Inc. is to produce software products that multiply the power and efficiency of empirical scientific research in the social sciences.</p>
      <p>A central goal is to expand access to complex data sources and to the advanced methods of scientific investigation needed to analyze them.</p>
    </div>
    <aside class="news">
      <h2>NEWS</h2>
      <p class="news-item"><strong>April, 2009</strong>An early access preview of the Velbris Data Manager is available.</p>
      <p class="news-item"><strong>May, 2008</strong>Plenary Session by Miriam Halvorsen - New approaches to complex data management</p>
      <p class="news-item">34TH ANNUAL CONFERENCE<br>IADSR 2008<br>May 27-30, 2008</p>
    </aside>
    <div class="cta">Preview Release Available!<br><span class="product">Velbris Data Manager</span><br>Download Preview Release</div>
    <svg class="cta-arrow" width="26" height="18" viewBox="0 0 26 18" aria-hidden="true"><path d="M1 1h6l8 8-8 8H1l8-8z M11 1h6l8 8-8 8h-6l8-8z" fill="var(--arrow)"/></svg>
    <div class="team-photo" role="img" aria-label="Black and white photo of a smiling businesswoman with colleagues behind her"></div>
    <div class="panel-foot"></div>
  </section>

</div>
</body>
</html>
```